A Book Cover For a Book Called "Tamsire"

Attached are two files for the ISBN bar graph for the print version of the cover! Same image, just two different formats.
Updates

Project Deadline Extended Reason: We'd like to see a few more designs, and work with a few of the designs already submitted. Added Tuesday, October 24, 2017

Target Market(s)

young adult female, parents

Colors

Designer to choose colors to be used in the design.

```html
<!DOCTYPE html>
<html lang="en">
<head>
<meta charset="utf-8">
<title>Tamsire — A Memoir</title>
<link rel="stylesheet" href="https://fonts.googleapis.com/css2?family=Parisienne&family=Sorts+Mill+Goudy:ital@0;1&display=swap">
<style>
  :root {
    --night: #1c212c;
    --slate: #3a4150;
    --mist: #6c7381;
    --satin: #c9a56e;
    --satin-light: #e8cf9c;
    --wood: #4a3a2a;
    --wood-dark: #241b14;
    --ink-light: #f4efe7;
  }
  html, body {
    margin: 0;
    padding: 0;
    width: 789px;
    height: 1200px;
    overflow: hidden;
    background: var(--night);
  }
  .cover {
    position: relative;
    width: 789px;
    height: 1200px;
    overflow: hidden;
  }
  .cover-art {
    position: absolute;
    inset: 0;
    background:
      radial-gradient(ellipse 210px 420px at 470px 640px, rgba(232,207,156,0.85), rgba(201,165,110,0.55) 45%, rgba(201,165,110,0) 100%),
      radial-gradient(ellipse 170px 360px at 230px 660px, rgba(201,165,110,0.65), rgba(150,120,80,0.35) 50%, rgba(150,120,80,0) 100%),
      radial-gradient(ellipse 260px 300px at 720px 560px, rgba(108,115,129,0.55), rgba(108,115,129,0) 100%),
      radial-gradient(ellipse 220px 300px at 40px 420px, rgba(90,98,112,0.5), rgba(90,98,112,0) 100%),
      linear-gradient(to bottom, var(--night) 0%, #262b36 30%, var(--slate) 55%, var(--wood) 78%, var(--wood-dark) 100%);
  }
  .cover-art::after {
    content: "";
    position: absolute;
    inset: 0;
    background: linear-gradient(to bottom, rgba(0,0,0,0) 70%, rgba(20,15,10,0.55) 100%);
  }
  .title {
    position: absolute;
    left: 90px;
    top: 62px;
    margin: 0;
    font-family: "Parisienne", cursive;
    font-weight: 400;
    font-size: 178px;
    line-height: 1;
    color: var(--ink-light);
    text-shadow: 0 2px 10px rgba(0,0,0,0.35);
  }
  .subtitle {
    position: absolute;
    right: 52px;
    top: 262px;
    margin: 0;
    font-family: "Sorts Mill Goudy", serif;
    font-style: italic;
    font-size: 24px;
    color: var(--ink-light);
  }
  .byline {
    position: absolute;
    left: 0;
    right: 0;
    top: 1018px;
    text-align: center;
    color: var(--ink-light);
    font-family: "Sorts Mill Goudy", serif;
  }
  .author {
    margin: 0;
    font-size: 50px;
    line-height: 1.1;
    letter-spacing: 0.5px;
  }
  .coauthor {
    margin: 4px 0 0;
    font-style: italic;
    font-size: 34px;
  }
</style>
</head>
<body>
  <main class="cover">
    <div class="cover-art" role="img" aria-label="Photograph of a worn pair of satin pointe shoes with loose ribbons standing on a wooden floor, lit warmly against a misty dark blue background"></div>
    <h1 class="title">Tamsire</h1>
    <p class="subtitle">A Memoir</p>
    <div class="byline">
      <p class="author">Maren Ashby</p>
      <p class="coauthor">with Lydia Colen</p>
    </div>
  </main>
</body>
</html>
```